Business Card Design

Cedar Gate Rentals
Cedar Gate Rentals is a high end home rental leasing company that provides exquisite properties in niche markets. We are a small family owned business that considers our clients not as renters, but as friends. Every property we buy must be brought up to our high standards before it is offered on the market. The properties that we lease are exceptional, "move in" ready homes. This allows for the client to take pride in their lease as if it was their own home. To put it another way; we do not lease a property that we would not live in ourselves.

Target Market(s)

Couples making $100K or more

Industry/Entity Type

Business

Requirements
Must have
• Some sort of logo
Nice to have
• good slogan
Should not have
• Pink

```html
<!DOCTYPE html>
<html lang="en">
<head>
<meta charset="utf-8">
<title>Cedar Gate Rentals – Business Card</title>
<link rel="stylesheet" href="https://fonts.googleapis.com/css2?family=Open+Sans:wght@400;600;700&display=swap">
<style>
  :root {
    --orange: #e8773a;
    --orange-deep: #d9572a;
    --ink: #3a3a3a;
    --ink-soft: #555555;
    --rule: #8a8a8a;
    --card: #ffffff;
    --backdrop: #e9e7e4;
  }
  * { margin: 0; padding: 0; box-sizing: border-box; }
  html, body { width: 1200px; height: 1023px; overflow: hidden; }
  body {
    background: var(--backdrop);
    font-family: "Open Sans", Arial, sans-serif;
    position: relative;
  }
  .card {
    position: absolute;
    left: 150px; top: 254px;
    width: 900px; height: 514px;
    background: linear-gradient(180deg, #ffffff 0%, #f4f4f4 100%);
    box-shadow: 0 6px 18px rgba(0,0,0,0.18);
    overflow: hidden;
  }
  .brand {
    position: absolute;
    right: 60px; top: 58px;
    display: flex; align-items: center; gap: 16px;
  }
  .brand-mark { width: 34px; height: 34px; background: var(--orange); }
  .brand-name {
    font-weight: 700; font-size: 36px; color: var(--ink);
    letter-spacing: 2px; text-transform: uppercase; line-height: 1;
  }
  .brand-rule {
    position: absolute; left: 290px; right: 60px; top: 122px;
    height: 1px; background: var(--rule);
  }
  .person { position: absolute; left: 60px; top: 148px; }
  .person-name {
    font-weight: 700; font-size: 31px; color: var(--orange);
    text-transform: uppercase; letter-spacing: 0.5px; line-height: 42px;
  }
  .person-role {
    display: flex; align-items: center; gap: 10px;
    margin-top: 6px; font-size: 19px; color: var(--ink-soft);
  }
  .person-role::before { content: ""; width: 26px; height: 1px; background: var(--ink-soft); }
  .person-role::after { content: ""; width: 110px; height: 1px; background: var(--rule); }
  .contacts { position: absolute; left: 60px; top: 272px; list-style: none; }
  .contacts li {
    display: flex; align-items: center; gap: 12px;
    font-size: 19px; color: var(--ink); line-height: 34px;
  }
  .contact-icon {
    width: 20px; height: 20px; background: var(--orange);
    border-radius: 3px; display: flex; align-items: center; justify-content: center;
  }
  .address { position: absolute; left: 540px; top: 272px; font-size: 19px; color: var(--ink); line-height: 30px; }
  .address-company { color: var(--orange); font-weight: 600; }
  .slogan-band {
    position: absolute; left: 0; right: 0; bottom: 0; height: 86px;
    background: linear-gradient(180deg, var(--orange) 0%, var(--orange-deep) 100%);
    display: flex; align-items: center; justify-content: center;
  }
  .slogan {
    font-weight: 600; font-size: 21px; color: var(--ink);
    text-transform: uppercase; letter-spacing: 0.5px;
  }
</style>
</head>
<body>
  <div class="card">
    <div class="brand">
      <div class="brand-mark"></div>
      <div class="brand-name">Cedar Gate Rentals</div>
    </div>
    <div class="brand-rule"></div>

    <div class="person">
      <div class="person-name">Daniel Hartley</div>
      <div class="person-role">Director</div>
    </div>

    <ul class="contacts">
      <li>
        <span class="contact-icon">
          <svg width="12" height="12" viewBox="0 0 12 12"><path d="M2.5 1 L4.5 1 L5.2 3.6 L4 4.6 Q5 7 7.4 8 L8.4 6.8 L11 7.5 L11 9.5 Q10.5 11 9 11 Q1 10 1 3 Q1 1.5 2.5 1Z" fill="#fff"/></svg>
        </span>
        215-555-0147
      </li>
      <li>
        <span class="contact-icon">
          <svg width="12" height="10" viewBox="0 0 12 10"><rect x="0.5" y="0.5" width="11" height="9" fill="none" stroke="#fff"/><path d="M0.5 0.5 L6 5.5 L11.5 0.5" fill="none" stroke="#fff"/></svg>
        </span>
        daniel@cedargaterentals.com
      </li>
      <li>
        <span class="contact-icon">
          <svg width="12" height="12" viewBox="0 0 12 12"><circle cx="6" cy="6" r="5" fill="none" stroke="#fff"/><ellipse cx="6" cy="6" rx="2.2" ry="5" fill="none" stroke="#fff"/><path d="M1 6 H11" stroke="#fff"/></svg>
        </span>
        www.cedargaterentals.com
      </li>
    </ul>

    <div class="address">
      <div class="address-company">Cedar Gate Rentals Ltd.</div>
      <div>48 Maple Row</div>
      <div>Linden, PA 19000</div>
    </div>

    <div class="slogan-band">
      <p class="slogan">We do not lease a property that we would not live in ourselves.</p>
    </div>
  </div>
</body>
</html>
```